Business Card Design - Law Firm

We are a boutique law firm located near the beach in Manly, Australia. We have recently had a new logo designed and are revamping our business cards with the new logo.

We have recently had a business card design done for us but are not entirely happy with it. We are looking for something modern, simplistic but striking. We would like to see multiple designs.

We have attached a word document which includes our new logo and the current business card design which we are looking at moving away from.

We would like the business cards to be double sided. We would like the design to include something which we can print in gloss colour when we send it to the business card printers.

```html
<!DOCTYPE html>
<html lang="en">
<head>
<meta charset="utf-8">
<title>Harlow &amp; Partners – Business Cards</title>
<link rel="stylesheet" href="https://fonts.googleapis.com/css2?family=Montserrat:ital,wght@0,400;0,500;0,600;1,400&display=swap">
<style>
  :root {
    --navy: #2a3a80;
    --navy-deep: #233170;
    --ink: #1d1d1f;
    --grey: #55585e;
    --paper: #ffffff;
    --backdrop: #ecebe8;
    --gold: #c4a86a;
  }
  * { box-sizing: border-box; margin: 0; padding: 0; }
  html, body {
    width: 1200px; height: 901px; overflow: hidden;
    background: var(--backdrop);
    font-family: "Montserrat", sans-serif;
  }
  .stage { position: relative; width: 1200px; height: 901px; }

  .card {
    position: absolute;
    width: 560px; height: 320px;
    box-shadow: 0 10px 28px rgba(0,0,0,.18);
  }

  /* Reverse side */
  .card--reverse {
    left: 90px; top: 110px;
    background: var(--navy);
    display: flex; align-items: center; justify-content: center;
  }
  .card--reverse .brand { color: var(--paper); font-size: 30px; }
  .card--reverse .brand-dot { background: var(--paper); width: 34px; height: 34px; }

  /* Front side */
  .card--front {
    left: 550px; top: 450px;
    background: var(--paper);
    padding: 40px 38px 0 44px;
  }
  .brand {
    display: flex; align-items: center; gap: 14px;
    font-weight: 500; letter-spacing: .02em; white-space: nowrap;
  }
  .brand-dot { border-radius: 50%; flex: none; }
  .card--front .brand { color: var(--navy); font-size: 20px; }
  .card--front .brand-dot { background: var(--navy); width: 24px; height: 24px; }

  .details {
    display: grid; grid-template-columns: 260px 1fr;
    margin-top: 74px;
  }
  .person { text-align: right; padding-right: 48px; padding-top: 4px; }
  .person-name { color: var(--navy); font-size: 22px; font-weight: 500; }
  .person-role { color: var(--grey); font-size: 13px; font-style: italic; margin-top: 2px; }

  .contact { font-size: 12.5px; color: var(--grey); line-height: 1.45; }
  .contact-firm { color: var(--navy); font-weight: 600; font-size: 13px; margin-bottom: 2px; }
  .contact-address { margin-bottom: 12px; }
  .contact-line strong { color: var(--navy); font-weight: 600; }
</style>
</head>
<body>
<main class="stage">
  <section class="card card--reverse" aria-label="Card reverse">
    <div class="brand"><span class="brand-dot"></span>Harlow &amp; Partners</div>
  </section>

  <section class="card card--front" aria-label="Card front">
    <div class="brand"><span class="brand-dot"></span>Harlow &amp; Partners</div>
    <div class="details">
      <div class="person">
        <p class="person-name">Megan Ashford</p>
        <p class="person-role">Practice Manager</p>
      </div>
      <div class="contact">
        <p class="contact-firm">Harlow &amp; Partners</p>
        <p class="contact-address">Suite 4, 18 Tidewater Lane<br>SEAVIEW NSW 2099</p>
        <p class="contact-line"><strong>Phone:</strong> (02) 9000 4821</p>
        <p class="contact-line"><strong>Email:</strong> megan.ashford@seaviewlaw.com.au</p>
        <p class="contact-line"><strong>Web:</strong> www.harlowandpartners.com.au</p>
      </div>
    </div>
  </section>
</main>
</body>
</html>
```